Business card design reauest

2 sided. White on both sides

Martin Oakhurst

Cedar Bay, Northland

Cell Phone / Whatsapp/ Wechat/Zalo
1-555-382-7194
Moakhurst@kvpartsline.vn
Www.kvpartsline.vn
Www.kvpartsline.com

Industry/Entity Type

Sofa and furniture and kitchen

Contact Information for Business Card

2 sided. White on both sides Martin Oakhurst Cedar Bay, Northland Cell Phone / Whatsapp/ Wechat/Zalo 1-555-382-7194 Moakhurst@kvpartsline.vn Www.kvpartsline.vn Www.kvpartsline.com

```html
<!DOCTYPE html>
<html lang="en">
<head>
<meta charset="utf-8">
<title>KV Partsline – Business Card</title>
<link href="https://fonts.googleapis.com/css2?family=Cinzel:wght@500&family=Tinos:wght@400;700&display=swap" rel="stylesheet">
<style>
  :root {
    --canvas: #e9eaeb;
    --card: #ffffff;
    --green: #1e9145;
    --ink: #2a2a2a;
    --rule: #333333;
    --shadow: rgba(0,0,0,0.18);
  }
  * { box-sizing: border-box; margin: 0; padding: 0; }
  html, body {
    width: 1200px; height: 900px; overflow: hidden;
    background: var(--canvas);
  }
  .canvas { position: relative; width: 1200px; height: 900px; }
  .card {
    position: absolute;
    width: 630px; height: 360px;
    background: linear-gradient(135deg, #f1f1f1 0%, var(--card) 55%);
    box-shadow: 0 10px 28px var(--shadow);
    overflow: hidden;
  }
  .card--front { left: 285px; top: 50px; }
  .card--back  { left: 285px; top: 470px; }

  .wordmark {
    font-family: "Cinzel", serif;
    font-weight: 500;
    color: var(--green);
    letter-spacing: 0.02em;
    white-space: nowrap;
  }
  .front-brand { position: absolute; left: 70px; top: 140px; }
  .front-brand .wordmark { font-size: 44px; line-height: 1; }
  .front-brand .underline {
    display: block; margin-top: 12px;
    width: 100%; height: 1.5px; background: var(--rule);
  }

  .back-brand {
    position: absolute; right: 50px; top: 44px;
    display: flex; align-items: center; gap: 10px;
  }
  .back-brand .dot { width: 14px; height: 14px; background: var(--green); }
  .back-brand .wordmark { font-size: 26px; line-height: 1; }

  .name-row {
    position: absolute; left: 40px; right: 0; top: 176px;
    display: flex; align-items: flex-end; gap: 10px;
  }
  .person-name {
    font-family: "Tinos", serif; font-weight: 700;
    color: var(--green); font-size: 21px; letter-spacing: 0.01em;
    white-space: nowrap; line-height: 1;
  }
  .name-rule { flex: 1; height: 1px; background: var(--green); margin-bottom: 8px; }

  .contacts {
    position: absolute; left: 44px; top: 212px;
    list-style: none;
    font-family: "Tinos", serif; font-size: 16px; color: var(--ink);
  }
  .contacts li { display: flex; align-items: center; gap: 9px; height: 25px; white-space: nowrap; }
  .contacts svg { width: 15px; height: 15px; flex: none; fill: none; stroke: var(--ink); stroke-width: 1.6; }
  .contacts .solid { fill: var(--ink); stroke: none; }
</style>
</head>
<body>
<main class="canvas">
  <section class="card card--front" aria-label="Card front">
    <div class="front-brand">
      <span class="wordmark">KV PARTSLINE</span>
      <span class="underline"></span>
    </div>
  </section>

  <section class="card card--back" aria-label="Card back">
    <div class="back-brand">
      <span class="dot"></span>
      <span class="wordmark">KV PARTSLINE</span>
    </div>

    <div class="name-row">
      <span class="person-name">MARTIN OAKHURST</span>
      <span class="name-rule"></span>
    </div>

    <ul class="contacts">
      <li>
        <svg viewBox="0 0 24 24"><path class="solid" d="M6.6 10.8a15 15 0 0 0 6.6 6.6l2.2-2.2c.3-.3.7-.4 1-.2 1.1.4 2.3.6 3.6.6.6 0 1 .4 1 1V20c0 .6-.4 1-1 1A17 17 0 0 1 3 4c0-.6.4-1 1-1h3.5c.6 0 1 .4 1 1 0 1.3.2 2.5.6 3.6.1.3 0 .7-.2 1z"/></svg>
        <span>1-555-382-7194</span>
      </li>
      <li>
        <svg viewBox="0 0 24 24"><path class="solid" d="M2 5h20v14H2z"/><path d="M2.5 5.5 12 13l9.5-7.5" stroke="#fff"/></svg>
        <span>Moakhurst@kvpartsline.vn</span>
      </li>
      <li>
        <svg viewBox="0 0 24 24"><circle cx="12" cy="12" r="9.5"/><ellipse cx="12" cy="12" rx="4" ry="9.5"/><path d="M2.5 12h19M4 7h16M4 17h16"/></svg>
        <span>Www.kvpartsline.vn</span>
      </li>
      <li>
        <svg viewBox="0 0 24 24"><circle cx="12" cy="12" r="9.5"/><ellipse cx="12" cy="12" rx="4" ry="9.5"/><path d="M2.5 12h19M4 7h16M4 17h16"/></svg>
        <span>Www.kvpartsline.com</span>
      </li>
      <li>
        <svg viewBox="0 0 24 24"><path class="solid" d="M12 2a7 7 0 0 0-7 7c0 5.2 7 13 7 13s7-7.8 7-13a7 7 0 0 0-7-7zm0 9.5A2.5 2.5 0 1 1 12 6.5a2.5 2.5 0 0 1 0 5z"/></svg>
        <span>Cedar Bay, Northland</span>
      </li>
    </ul>
  </section>
</main>
</body>
</html>
```